Letterhead Design

We need a new Letterhead design for a 30 year old Electrical Company. We service domestic and commercial places. We have a logo recently made so to incorporate that. Using same colours or interested to see others added.
Would like to see a couple of options with all the info in letterhead, then another with info in a footnote down the bottom.

info needed to be added:

-Lic. No 48162
8/22-24 Larkin Rd, Tolvern 2087
W - brightcoilpower.com.au
T - (02) 9471 3825
M - 0427 593 168
E - info@brightcoilpower.com.au
ABN: 42 597 214 630

Electrical

```html
<!DOCTYPE html>
<html lang="en">
<head>
<meta charset="utf-8">
<title>Brightcoil Power Electrical – Letterhead and Folder</title>
<link href="https://fonts.googleapis.com/css2?family=Didact+Gothic&family=Libre+Baskerville:wght@400;700&display=swap" rel="stylesheet">
<style>
  :root {
    --backdrop: #e6e9ea;
    --charcoal: #2b2b2c;
    --orange: #ff9514;
    --orange-deep: #ff8a0f;
    --paper: #ffffff;
    --ink: #3a3a3a;
    --faint: #e4e4e4;
  }
  * { margin: 0; padding: 0; box-sizing: border-box; }
  html, body { width: 1200px; height: 784px; overflow: hidden; }
  body {
    background: var(--backdrop);
    position: relative;
    font-family: "Didact Gothic", "Century Gothic", sans-serif;
  }
  .letterhead {
    position: absolute; left: 42px; top: 45px;
    width: 513px; height: 696px;
    background: var(--paper);
    border-radius: 14px; overflow: hidden;
    box-shadow: 0 2px 6px rgba(0,0,0,.18);
  }
  .letterhead .top-band, .letterhead .bottom-band { position: absolute; left: 0; }
  .letterhead .top-band { top: 0; }
  .letterhead .bottom-band { bottom: 0; }
  .brand-name {
    font-family: "Libre Baskerville", Georgia, serif;
    font-weight: 400; white-space: nowrap;
  }
  .letterhead .header-name {
    position: absolute; left: 48px; top: 16px;
    color: var(--paper); font-size: 17px;
  }
  .address {
    position: absolute; right: 14px; top: 17px;
    color: var(--paper); font-family: "Libre Baskerville", Georgia, serif;
    font-size: 7.5px; font-weight: 700;
  }
  .contacts {
    position: absolute; right: 14px; top: 33px;
    display: flex; gap: 14px;
    color: var(--paper); font-family: "Libre Baskerville", Georgia, serif;
    font-size: 8px;
  }
  .contacts span { display: flex; align-items: center; gap: 5px; }
  .contacts svg { fill: var(--orange); }
  .watermark {
    position: absolute; left: 62px; top: 330px;
    color: var(--faint); font-size: 33px;
  }
  .body-copy {
    position: absolute; left: 48px; top: 144px; width: 425px;
    color: var(--ink); font-size: 10.6px; line-height: 17.4px;
    text-align: justify;
  }
  .body-copy p + p { margin-top: 17.4px; }
  .signature { position: absolute; left: 383px; top: 584px; color: var(--ink); }
  .signature .name { font-size: 14px; }
  .signature .role { font-size: 9.5px; margin-top: 5px; }
  .footer-watermark {
    position: absolute; left: 48px; top: 609px;
    color: var(--faint); font-size: 17px;
  }
  .website {
    position: absolute; left: 46px; bottom: 9px;
    color: var(--paper); font-family: "Libre Baskerville", Georgia, serif;
    font-size: 7.5px; letter-spacing: 1.3px;
  }
  .licence {
    position: absolute; right: 37px; bottom: 12px; text-align: right;
    font-family: "Libre Baskerville", Georgia, serif; font-size: 7.5px; line-height: 13px;
  }
  .licence .lic { color: var(--paper); }
  .licence .abn { color: var(--orange); }
  .folder {
    position: absolute; left: 634px; top: 44px;
    width: 513px; height: 697px; border-radius: 14px;
    background: linear-gradient(180deg, var(--orange) 0%, var(--orange-deep) 100%);
    box-shadow: 0 2px 6px rgba(0,0,0,.18);
  }
  .folder .pocket { position: absolute; right: 0; top: 150px; }
  .folder .cover-name {
    position: absolute; left: 122px; top: 518px;
    color: var(--charcoal); font-size: 30px;
  }
</style>
</head>
<body>
  <section class="letterhead">
    <svg class="top-band" width="513" height="130" viewBox="0 0 513 130" aria-hidden="true">
      <path d="M0 0H513V58H440Q160 60 0 92Z" fill="var(--charcoal)"/>
      <path d="M0 98Q170 66 410 66Q170 74 0 112Z" fill="var(--orange)"/>
    </svg>
    <div class="brand-name header-name">Brightcoil Power Electrical</div>
    <div class="address">8/22-24 Larkin Rd, Tolvern 2087</div>
    <div class="contacts">
      <span><svg width="9" height="9" viewBox="0 0 24 24"><path d="M6.6 10.8a15 15 0 006.6 6.6l2.2-2.2a1 1 0 011-.25 11.4 11.4 0 003.6.57 1 1 0 011 1V20a1 1 0 01-1 1A17 17 0 013 4a1 1 0 011-1h3.5a1 1 0 011 1c0 1.25.2 2.45.57 3.57a1 1 0 01-.25 1z"/></svg>(02) 9471 3825</span>
      <span><svg width="7" height="10" viewBox="0 0 14 20"><path d="M2 0h10a2 2 0 012 2v16a2 2 0 01-2 2H2a2 2 0 01-2-2V2a2 2 0 012-2zm0 3v12h10V3z"/></svg>0427 593 168</span>
      <span><svg width="10" height="8" viewBox="0 0 20 16"><path d="M0 0h20v16H0zM2 2v1l8 6 8-6V2z"/></svg>info@brightcoilpower.com.au</span>
    </div>

    <div class="brand-name watermark">Brightcoil Power</div>

    <div class="body-copy">
      <p>Lorem ipsum dolor sit amet, consectetur adipiscing elit. Donec orci purus, luctus vitae dignissim eu, iaculis sed purus. Vivamus faucibus, ipsum nec aliquet viverra, leo mauris condimentum ligula, sit amet sagittis enim ligula quis arcu. Nam egestas tortor id nisi porttitor mattis. In tortor ante, ultricies in suscipit a, tempus non massa. Vivamus et auctor mi. Fusce vel massa nulla. Phasellus nec eros mauris, et scelerisque orci. Donec malesuada orci vitae nulla accumsan porta a id massa.</p>
      <p>Quisque accumsan iaculis magna sit amet fringilla. Maecenas consequat, magna eget tincidunt semper, odio nibh rutrum mi, id feugiat ante nisi eu risus. Vestibulum nunc orci, rhoncus a placerat in, ultricies in mi. Cras mattis varius eros, vel fringilla nisi suscipit eget. Quisque scelerisque sagittis nulla at porttitor. Mauris a justo et tellus interdum tristique. Sed id augue vitae urna euismod commodo aliquet a quam. Pellentesque arcu velit, cursus et malesuada ut, consequat et diam. Nullam erat sem, rhoncus id ullamcorper vitae, rhoncus et arcu. In ultricies ultricies nulla.</p>
      <p>Kut rutrum nisi iaculis at. Donec eu magna a metus ornare faucibus. Fusce aliquet faucibus ultricies. Morbi semper, est id tincidunt gravida, sem arcu adipiscing lacus, ac bibendum nulla leo eu purus. Quisque nec diam sed risus consectetur a ccumsan quis quis nibh. Vestibulum id purus lorem. Donec eu magna a metus ornare faucibus. Fusce aliquet faucibus ultricies. Morbi semper, est id tincidunt gravida, sem arcu adipiscing lacus, ac bibendum nulla leo eu purus. Quisque nec diam sed risus consectetur a ccumsan quis quis nibh. Vestibulum id purus lorem.</p>
    </div>

    <div class="signature">
      <div class="name">Liam Hartley</div>
      <div class="role">Co-Founder &amp; CEO</div>
    </div>

    <div class="brand-name footer-watermark">Brightcoil Power</div>

    <svg class="bottom-band" width="513" height="90" viewBox="0 0 513 90" aria-hidden="true">
      <path d="M0 66H120Q330 62 513 30V90H0Z" fill="var(--charcoal)"/>
      <path d="M98 64Q340 56 513 14V30Q330 62 98 64Z" fill="var(--orange)"/>
    </svg>
    <div class="website">www.brightcoilpower.com.au</div>
    <div class="licence">
      <div class="lic">Lic. No 48162</div>
      <div class="abn">ABN: 42 597 214 630</div>
    </div>
  </section>

  <section class="folder">
    <svg class="pocket" width="36" height="230" viewBox="0 0 36 230" aria-hidden="true">
      <path d="M36 0V230H0V40Q0 20 20 12Z" fill="rgba(255,120,0,.35)"/>
    </svg>
    <div class="brand-name cover-name">Brightcoil Power</div>
  </section>
</body>
</html>
```